Brightwell Pictures Business Card

Hello,

i would like to have a dynamic, creative but tasteful card, colour used, front and back. I have attached a sample card that I liked very much from another individual to give you an idea of the theme/approach, but not colour. Ideally the graphic elements of the Brightwell Logo are brought into the design.

Target Market(s)

North America

Industry/Entity Type

Film Production

Contact Information for Business Card

Mirela Vantasch
President/Founder
Brightwell Pictures Inc.
587 914 3362
mirela@brightwellpix.tv

Font styles to use
Sans Serif

Colors
6b449b
5c5c5c
fdfdfd
000000

Requirements
Must have
• Logo, name, Company name, email and cell number. no Address line to be included.
Should not have
• any unrelated GFX elements, serif fonts

```html
<!DOCTYPE html>
<html lang="en">
<head>
<meta charset="utf-8">
<title>Brightwell Pictures Business Card</title>
<link href="https://fonts.googleapis.com/css2?family=Open+Sans:wght@400;600;700;800&display=swap" rel="stylesheet">
<style>
  :root {
    --purple: #6b449b;
    --purple-deep: #5a2f92;
    --purple-light: #7d55b0;
    --grey: #5c5c5c;
    --grey-soft: #8a8a8a;
    --paper: #fdfdfd;
    --ink: #000000;
    --name-ink: #333333;
    --backdrop: #1c1b21;
  }
  html, body {
    margin: 0;
    padding: 0;
    width: 1200px;
    height: 864px;
    overflow: hidden;
    background: var(--backdrop);
    font-family: "Open Sans", Arial, sans-serif;
  }
  .canvas {
    width: 1200px;
    height: 864px;
    display: flex;
    flex-direction: column;
    align-items: center;
    justify-content: center;
    gap: 40px;
  }
  .card {
    width: 640px;
    height: 366px;
    border-radius: 22px;
    position: relative;
    overflow: hidden;
    box-sizing: border-box;
  }
  .card-front {
    background: var(--purple-deep);
    display: flex;
    align-items: center;
    justify-content: center;
  }
  .front-pattern {
    position: absolute;
    inset: 0;
    background: radial-gradient(ellipse at 50% 45%, var(--purple-light) 0%, var(--purple) 45%, var(--purple-deep) 100%);
  }
  .wordmark {
    position: relative;
    font-weight: 800;
    letter-spacing: -1px;
    line-height: 1;
    white-space: nowrap;
  }
  .card-front .wordmark {
    color: var(--paper);
    font-size: 64px;
  }
  .card-back {
    background: var(--paper);
    display: flex;
    align-items: center;
  }
  .brand-block {
    width: 330px;
    display: flex;
    align-items: center;
    justify-content: center;
  }
  .card-back .wordmark {
    color: var(--grey);
    font-size: 50px;
  }
  .divider {
    width: 1px;
    height: 130px;
    background: var(--grey-soft);
  }
  .contact {
    padding-left: 28px;
    color: var(--grey);
    font-size: 13.5px;
    line-height: 1.45;
  }
  .contact p { margin: 0; }
  .contact-name {
    margin: 0;
    font-size: 22px;
    font-weight: 700;
    color: var(--name-ink);
    line-height: 1.2;
  }
  .contact .contact-title {
    margin: 0 0 6px;
    font-size: 15px;
    font-weight: 600;
    color: var(--purple);
  }
  .contact-lines { margin-top: 8px; }
  .contact-line {
    display: flex;
    align-items: center;
    gap: 8px;
  }
  .contact-line svg { width: 12px; height: 12px; flex: none; }
</style>
</head>
<body>
<main class="canvas">
  <section class="card card-front" aria-label="Card front">
    <div class="front-pattern" role="img" aria-label="Soft purple gradient field with brand shutter blade shapes"></div>
    <span class="wordmark">Brightwell</span>
  </section>

  <section class="card card-back" aria-label="Card back">
    <div class="brand-block">
      <span class="wordmark">Brightwell</span>
    </div>
    <div class="divider"></div>
    <div class="contact">
      <h1 class="contact-name">Mirela Vantasch</h1>
      <p class="contact-title">President/Founder</p>
      <p class="contact-company">Brightwell Pictures Inc.</p>
      <div class="contact-lines">
        <p class="contact-line">
          <svg viewBox="0 0 12 12" aria-hidden="true"><path d="M2.5 1 L4.5 1 L5.3 3.4 L4 4.4 C4.6 5.8 6.2 7.4 7.6 8 L8.6 6.7 L11 7.5 L11 9.5 C11 10.3 10.3 11 9.5 11 C5 11 1 7 1 2.5 C1 1.7 1.7 1 2.5 1 Z" fill="var(--purple)"/></svg>
          587 914 3362
        </p>
        <p class="contact-line">
          <svg viewBox="0 0 12 12" aria-hidden="true"><rect x="0.5" y="2" width="11" height="8" rx="1" fill="var(--purple)"/><path d="M1 2.6 L6 6.6 L11 2.6" stroke="var(--paper)" stroke-width="1" fill="none"/></svg>
          mirela@brightwellpix.tv
        </p>
      </div>
    </div>
  </section>
</main>
</body>
</html>
```